Racing Simulator Website

We're a new startup designing, selling, and supporting racing simulators, specifically targeted at Track Day enthusiasts and Club Racers alike. We are differentiating ourselves from other Racing Simulator companies by fully supporting the software and hardware of our systems. The client does not need to update their software to keep the simulator running, and any issues they may run into with the hardware, we will fix. We've designed our systems with this in mind and have added features that make it as easy for the client to operate as possible. Our current website says this but doesn't do a good job of highlighting how much easier these extra features make the simulator to live with.

Our systems look like a single console in the sense that the user neither sees nor interacts with the computer underneath but just uses the simulator using a simple button box. Our computers are connected to our cloud to keep Windows, the device drivers, and all the supported simulation games up to date, so that the system is always ready to use. Furthermore, we offer our systems as "lease-to-own" with small down payment and monthly installments, which also cover the ongoing hardware and software support for the duration of the lease. All other turnkey racing simulators require the full amount to be paid up front and do not offer software support to keep the systems up to date or provide anything beyond warranty service on the hardware.

We already have a website that contains most of this information, but it is not exciting. We're engineers building the systems but frankly do not know how to make our website exciting and compelling. We want the Home page experience to be much richer and ideally carry all these points across.

As we target track-day enthusiasts and club racers, we are positioning our simulators as tools to improve your technique and reflexes to improve your driving on the real track.
Our current website is here https://www.bluefernmotion.com
We already have more photos than what is currently on the website that you can use, or feel free to request specific photos of the system.

```html
<!DOCTYPE html>
<html lang="en">
<head>
<meta charset="utf-8">
<title>Blue Fern Motion – Racing Simulators</title>
<link href="https://fonts.googleapis.com/css2?family=Montserrat:wght@400;500;600;700&display=swap" rel="stylesheet">
<style>
:root{
  --navy:#173a5a;
  --navy-dark:#0f2c47;
  --yellow:#f4b942;
  --text:#1f2a36;
  --muted:#5d6670;
  --line:#c9ced4;
  --white:#ffffff;
}
*{box-sizing:border-box;margin:0;padding:0}
html,body{width:1200px;height:3967px;overflow:hidden}
body{font-family:"Montserrat",sans-serif;color:var(--text);background:var(--white);position:relative}
.abs{position:absolute}
.btn{position:absolute;background:var(--yellow);color:var(--navy-dark);font-size:15px;font-weight:500;padding:7px 16px;line-height:20px}
h2.section-title{position:absolute;left:0;width:1200px;text-align:center;font-size:36px;font-weight:600;color:var(--navy)}
p{font-size:14px;line-height:24px;color:var(--muted)}

/* header */
.site-header{position:absolute;top:0;left:0;width:1200px;height:82px;border-top:4px solid var(--yellow);background:var(--white)}
.brand{position:absolute;left:111px;top:20px;display:flex;align-items:center;gap:10px;font-size:26px;font-weight:700;color:var(--navy)}
.brand .mark{width:18px;height:18px;background:var(--yellow)}
.main-nav{position:absolute;right:111px;top:28px;display:flex;gap:34px;font-size:15px;color:var(--text)}
.main-nav .active{font-weight:600;border-bottom:2px solid var(--text);padding-bottom:3px}

/* hero */
.hero{position:absolute;top:82px;left:0;width:1200px;height:497px;background:linear-gradient(135deg,#1d4468,#143554);overflow:hidden}
.hero-circle{position:absolute;left:905px;top:-40px;width:340px;height:340px;border-radius:50%;background:var(--yellow)}
.hero-photo{position:absolute;left:680px;top:40px;width:390px;height:440px;background:radial-gradient(ellipse at center,#4a4a48 0%,#2c2c2b 55%,rgba(30,30,30,0) 75%)}
.hero h1{position:absolute;left:111px;top:84px;font-size:45px;line-height:52px;font-weight:700;color:var(--white)}
.hero p{position:absolute;left:111px;top:258px;width:520px;font-size:15px;line-height:26px;color:#e6ecf2}

/* what we do */
.problem-photo{position:absolute;left:60px;top:708px;width:620px;height:316px;background:linear-gradient(180deg,#f2f3f4,#d9dbdd 70%,#ffffff)}
.problem-title{position:absolute;left:635px;top:762px;width:460px;font-size:22px;line-height:31px;font-weight:500;color:var(--text)}
.problem-text{position:absolute;left:635px;top:834px;width:455px}
.solution-title{position:absolute;left:0;top:1096px;width:1200px;text-align:center;font-size:22px;font-weight:500}
.solution-text{position:absolute;left:190px;top:1140px;width:820px;text-align:center}
.feature-card{position:absolute;top:1234px;width:304px;height:249px;border:1px solid #7d8690;text-align:center;background:var(--white)}
.feature-card .icon{width:104px;height:104px;border-radius:50%;background:#d9dde2;margin:14px auto 0;display:flex;align-items:center;justify-content:center}
.feature-card h3{font-size:17px;line-height:21px;font-weight:500;margin-top:20px;color:var(--text)}
.feature-card p{font-size:13px;line-height:22px;margin:12px 20px 0}
.feature-card.highlight{background:linear-gradient(160deg,#2a4a68,#1a3a5a);border-color:var(--navy)}
.feature-card.highlight .icon{background:var(--white)}
.feature-card.highlight h3,.feature-card.highlight p{color:var(--white)}

/* sim racing */
.sim-band{position:absolute;top:1569px;left:0;width:1200px;height:1138px;background:linear-gradient(160deg,#f3e1da 0%,#ede3dc 40%,#efe7df 70%,#f3e4dc 100%)}
.sim-title{position:absolute;left:111px;top:1648px;font-size:36px;font-weight:600;color:var(--navy)}
.sim-text{position:absolute;left:111px;top:1714px;width:555px;color:#55606b}
.sim-frame-back{position:absolute;left:707px;top:1680px;width:356px;height:275px;background:var(--yellow)}
.sim-frame{position:absolute;left:722px;top:1643px;width:368px;height:295px;background:var(--white);padding:12px}
.sim-photo{width:100%;height:100%;background:linear-gradient(180deg,#cfd0d2,#8f9497 55%,#3a3c3e)}

.model-tabs{position:absolute;left:376px;top:2117px;display:flex;border:1px solid #8a939c;background:var(--white)}
.model-tabs span{font-size:15px;padding:8px 15px;line-height:20px}
.model-tabs .active{background:var(--navy);color:var(--white);font-weight:500}
.models-text{position:absolute;left:180px;top:2176px;width:840px;text-align:center}
.model-photo{position:absolute;top:2254px;height:294px}
.arrow{position:absolute;top:2376px;width:50px;height:50px;border-radius:50%;border:2px solid var(--navy);display:flex;align-items:center;justify-content:center}
.arrow.next{background:var(--navy)}

/* coaching */
.coach-photo{position:absolute;left:130px;top:2823px;width:390px;height:390px;border-radius:50%;background:linear-gradient(180deg,#dfe2e5 0%,#b9434a 55%,#8e2930 100%)}
.dot-grid{position:absolute;left:83px;top:2934px}
.coach-title{position:absolute;left:574px;top:2822px;font-size:36px;line-height:44px;font-weight:600;color:var(--navy)}
.coach-text{position:absolute;left:574px;top:2935px;width:516px}
.coach-text p+p{margin-top:6px}

/* testimonials */
.review-card{position:absolute;top:3376px;width:304px;height:206px;border:1px solid #7d8690;background:var(--white);padding:16px 15px}
.review-head{display:flex;align-items:center;gap:12px}
.avatar{width:52px;height:52px;border-radius:50%;background:#c7ccd1}
.review-head .name{font-size:15px;font-weight:500}
.review-head .time{font-size:11px;color:#8a9299}
.badge{margin-left:auto;width:28px;height:28px;border-radius:50%;border:3px solid #c9ced4}
.stars{margin-top:14px;display:flex;gap:2px}
.review-card p{font-size:12px;line-height:18px;color:#444c54;margin-top:14px}
.pager{position:absolute;top:3606px;left:565px;display:flex;gap:8px;align-items:center}
.pager span{width:10px;height:10px;border-radius:50%;background:#4d5761}
.pager span.on{width:14px;height:14px;background:var(--yellow)}

/* footer */
.site-footer{position:absolute;top:3708px;left:0;width:1200px;height:259px;background:linear-gradient(135deg,#1d4468,#143554);color:var(--white)}
.footer-brand{position:absolute;left:0;width:1200px;top:64px;display:flex;justify-content:center;align-items:center;gap:12px;font-size:40px;font-weight:700}
.footer-brand .mark{width:22px;height:22px;background:var(--white)}
.footer-nav{position:absolute;left:0;width:1200px;top:172px;display:flex;justify-content:center;gap:35px;font-size:15px}
.footer-rule{position:absolute;left:111px;width:978px;top:203px;border-top:1px solid rgba(255,255,255,.4)}
.copyright{position:absolute;left:0;width:1200px;top:221px;text-align:center;font-size:12px;color:#dfe6ee}
</style>
</head>
<body>

<header class="site-header">
  <div class="brand"><span class="mark"></span>Blue Fern Motion</div>
  <nav class="main-nav">
    <span class="active">Home</span><span>What We Do</span><span>What is Sim Racing</span><span>Models</span><span>Coaching</span>
  </nav>
</header>

<section class="hero">
  <div class="hero-circle"></div>
  <div class="hero-photo" role="img" aria-label="Black aluminium racing simulator rig with seat, wheel and monitor"></div>
  <h1>Train Like You Race.<br>Drive Every Track, Any<br>Time.</h1>
  <p>Professional-grade racing simulators — fully supported, always ready, built for serious drivers.</p>
  <span class="btn" style="left:111px;top:338px">Explore Simulators</span>
</section>

<h2 class="section-title" style="top:652px">What We Do</h2>
<div class="problem-photo" role="img" aria-label="Prebuilt turnkey simulator with triple monitors and racing seat"></div>
<h3 class="problem-title">The Problem with Traditional Turnkey Simulators</h3>
<p class="problem-text">Many prebuilt, turnkey simulators promise an easy setup, but they come with hidden complications. Over time, users find themselves struggling with software updates, compatibility issues, and troubleshooting technical problems rather than racing. Without external support, maintaining these systems can become a frustrating challenge.</p>

<h3 class="solution-title">Our Solution: A True Turnkey Experience</h3>
<p class="solution-text">We set out to build the easiest-to-use racing simulators on the market, ensuring that every driver - whether a seasoned racer or a track-day enthusiast - can focus on performance rather than maintenance.</p>

<div class="feature-card" style="left:111px">
  <div class="icon"><svg width="54" height="54" viewBox="0 0 54 54" fill="none" stroke="#173a5a" stroke-width="2"><circle cx="27" cy="18" r="9"/><path d="M23 18l3 3 5-6"/><path d="M6 30l8 10h10M48 30l-8 10H30"/><path d="M14 46h26"/></svg></div>
  <h3>Effortless<br>Setup &amp; Operation</h3>
  <p>Just jump in and race, no complicated configurations required.</p>
</div>
<div class="feature-card highlight" style="left:448px">
  <div class="icon"><svg width="54" height="54" viewBox="0 0 54 54" fill="none" stroke="#173a5a" stroke-width="2"><circle cx="27" cy="27" r="18"/><circle cx="27" cy="23" r="6"/><path d="M16 40c3-6 8-8 11-8s8 2 11 8"/></svg></div>
  <h3>Cloud-Based System<br>Management</h3>
  <p>We handle updates, driver settings, and optimizations remotely.</p>
</div>
<div class="feature-card" style="left:785px">
  <div class="icon"><svg width="54" height="54" viewBox="0 0 54 54" fill="none" stroke="#173a5a" stroke-width="2"><path d="M12 44V28h7v16zM19 30l7-12c2-3 6-2 5 2l-2 7h10c3 0 4 3 3 5l-3 9c-1 2-2 3-4 3H19"/><path d="M16 10l2 4 4 1-3 3 1 4-4-2-4 2 1-4-3-3 4-1zM38 10l2 4 4 1-3 3 1 4-4-2-4 2 1-4-3-3 4-1z"/></svg></div>
  <h3>Hassle-Free<br>Maintenance</h3>
  <p>No need to troubleshoot! We ensure everything is always up to date.</p>
</div>

<div class="sim-band" role="img" aria-label="Softly blurred racing cockpit background"></div>
<h2 class="sim-title">What is Sim Racing?</h2>
<p class="sim-text">Racing simulators have been around for quite some time. While their ability to simulate the driving experience has dramatically improved since they first appeared, the main components are basically the same. There are controllers that look and feel like controls in a car; pedals, a steering wheel, a shifter and maybe some more buttons that would control certain aspects such as traction control, etc. All these controls are arranged in a chassis, with a driver's seat, speakers and monitor(s) completing the experience of a car.</p>
<span class="btn" style="left:111px;top:1921px">Read More</span>
<div class="sim-frame-back"></div>
<div class="sim-frame"><div class="sim-photo" role="img" aria-label="Cockpit view of a simulator with wheel and ultrawide screen showing a race track"></div></div>

<h2 class="section-title" style="top:2028px">Our Models</h2>
<div class="model-tabs"><span>BFM Premium Simulator</span><span class="active">BFM Entry Simulator</span></div>
<p class="models-text">Lorem ipsum dolor sit amet, consectetur adipiscing elit, sed do eiusmod tempor incididunt ut labore et dolore magna aliqua. Ut enim ad minim veniam, quis nostrud exercitation ullamco laboris nisi</p>
<div class="model-photo" style="left:111px;width:223px;background:linear-gradient(135deg,#e6e7e8,#6f7275 60%,#1e1f20)" role="img" aria-label="Close-up of wheel base motor on simulator frame"></div>
<div class="model-photo" style="left:368px;width:465px;background:linear-gradient(180deg,#e8e9ea 0%,#a8b0b6 35%,#2a2c2e 60%,#d7d8d9 100%)" role="img" aria-label="Entry simulator cockpit with curved screen and wheel"></div>
<div class="model-photo" style="left:866px;width:223px;background:linear-gradient(135deg,#e0e1e2,#3a3b3d 60%,#141415)" role="img" aria-label="Pedal set mounted on simulator frame"></div>
<div class="arrow" style="left:43px"><svg width="18" height="18" viewBox="0 0 18 18"><path d="M12 2L5 9l7 7" fill="none" stroke="#173a5a" stroke-width="2"/></svg></div>
<div class="arrow next" style="left:1107px"><svg width="18" height="18" viewBox="0 0 18 18"><path d="M6 2l7 7-7 7" fill="none" stroke="#fff" stroke-width="2"/></svg></div>
<span class="btn" style="left:527px;top:2588px">Explore More</span>

<svg class="dot-grid" width="60" height="170" viewBox="0 0 60 170" fill="#1f2a36">
  <g><circle cx="3" cy="3" r="2.5"/><circle cx="29" cy="3" r="2.5"/><circle cx="55" cy="3" r="2.5"/>
  <circle cx="3" cy="30" r="2.5"/><circle cx="29" cy="30" r="2.5"/><circle cx="55" cy="30" r="2.5"/>
  <circle cx="3" cy="57" r="2.5"/><circle cx="29" cy="57" r="2.5"/><circle cx="55" cy="57" r="2.5"/>
  <circle cx="3" cy="84" r="2.5"/><circle cx="29" cy="84" r="2.5"/><circle cx="55" cy="84" r="2.5"/>
  <circle cx="3" cy="111" r="2.5"/><circle cx="29" cy="111" r="2.5"/><circle cx="55" cy="111" r="2.5"/>
  <circle cx="3" cy="138" r="2.5"/><circle cx="29" cy="138" r="2.5"/><circle cx="55" cy="138" r="2.5"/>
  <circle cx="3" cy="165" r="2.5"/><circle cx="29" cy="165" r="2.5"/><circle cx="55" cy="165" r="2.5"/></g>
</svg>
<div class="coach-photo" role="img" aria-label="Racing driver in red race suit and helmet"></div>
<h2 class="coach-title">Want To Improve<br>Your Driving?</h2>
<div class="coach-text">
  <p>Blue Fern Motion is proud to offer 1-on-1 coaching for sim racing from our very own Dan Keller. Dan has been instructing at Apex Line Racing School for over 2 years and in that time has also competed in many races and won multiple Spec Coupe races.</p>
  <p>Although sim racing is done through a completely different medium than real life racing, the driving techniques and strategies are near identical.</p>
</div>
<span class="btn" style="left:574px;top:3125px">Contact Us</span>

<h2 class="section-title" style="top:3290px">Our Testimonials</h2>
<div class="review-card" style="left:111px">
  <div class="review-head"><div class="avatar" role="img" aria-label="Reviewer portrait"></div><div><div class="name">Mark Delaney</div><div class="time">a month ago</div></div><div class="badge"></div></div>
  <div class="stars"><svg width="82" height="14" viewBox="0 0 82 14" fill="#f4b942"><path id="s" d="M7 0l2 4.5 5 .5-3.8 3.3 1.1 4.9L7 10.7 2.7 13.2l1.1-4.9L0 5l5-.5z"/><use href="#s" x="17"/><use href="#s" x="34"/><use href="#s" x="51"/><use href="#s" x="68"/></svg></div>
  <p>Lorem ipsum dolor sit amet, consectetur adipiscing elit, sed do eiusmod tempor incididunt ut labore et dolore magna aliqua. Quis ipsum suspendisse ultrices gravida.</p>
</div>
<div class="review-card" style="left:448px">
  <div class="review-head"><div class="avatar" role="img" aria-label="Reviewer portrait"></div><div><div class="name">Mark Delaney</div><div class="time">a month ago</div></div><div class="badge"></div></div>
  <div class="stars"><svg width="82" height="14" viewBox="0 0 82 14" fill="#f4b942"><use href="#s"/><use href="#s" x="17"/><use href="#s" x="34"/><use href="#s" x="51"/><use href="#s" x="68"/></svg></div>
  <p>Lorem ipsum dolor sit amet, consectetur adipiscing elit, sed do eiusmod tempor incididunt ut labore et dolore magna aliqua. Quis ipsum suspendisse ultrices gravida.</p>
</div>
<div class="review-card" style="left:785px">
  <div class="review-head"><div class="avatar" role="img" aria-label="Reviewer portrait"></div><div><div class="name">Mark Delaney</div><div class="time">a month ago</div></div><div class="badge"></div></div>
  <div class="stars"><svg width="82" height="14" viewBox="0 0 82 14" fill="#f4b942"><use href="#s"/><use href="#s" x="17"/><use href="#s" x="34"/><use href="#s" x="51"/><use href="#s" x="68"/></svg></div>
  <p>Lorem ipsum dolor sit amet, consectetur adipiscing elit, sed do eiusmod tempor incididunt ut labore et dolore magna aliqua. Quis ipsum suspendisse ultrices gravida.</p>
</div>
<div class="pager"><span class="on"></span><span></span><span></span><span></span></div>

<footer class="site-footer">
  <div class="footer-brand"><span class="mark"></span>Blue Fern Motion</div>
  <nav class="footer-nav"><span>Home</span><span>What We Do</span><span>What is Sim Racing</span><span>Models</span><span>Coaching</span></nav>
  <div class="footer-rule"></div>
  <div class="copyright">© 2025 Blue Fern Motion. All rights reserved.</div>
</footer>

</body>
</html>
```